Redesign for Popular UK Town Website

We're looking for someone to redesign a website for a popular tourist town that's visited by over 250,000 people a year. We have a basic design frame in place and need someone to make it look more 'professional.'
We've created a temporary design layout to show you a general idea of what we're looking for: http://dorrin.co.uk/
All text/images are placeholder images so you can get an idea of the general layout.
(Please note that you can grab any images found on the internet for 'tenby' to be used as placeholder images. This is because we will be visiting the locations and taking our own photos, after the design is complete.)
Target Market(s)
Tourists
Industry/Entity Type
Town
Number of Pages Required
2 page
Requirements
Must have
- You need to redesign the homepage: http://dorrin.co.uk/
- You also need to redesign the following page: http://dorrin.co.uk/hotels/ (This page will be used for multiple categories and is used to list locations of properties/places etc.)
- Design must be responsive also.
Nice to have
- Please feel free to add as much as you can to the content/features as with our limited knowledge of websites, have only been able to create a basic layout.

```html
<!DOCTYPE html>
<html lang="en">
<head>
<meta charset="utf-8">
<title>Dorrin – Come, Discover Dorrin</title>
<link rel="stylesheet" href="https://fonts.googleapis.com/css2?family=Roboto:wght@400;500;700;900&display=swap">
<style>
:root{
  --blue:#2ea3e6;
  --blue-dark:#1d86c4;
  --nav-active:#5dbbf0;
  --navy:#1c2431;
  --green:#5fa84f;
  --hero-accent:#6ad24d;
  --ink:#1d1d1f;
  --body:#555;
  --muted:#777;
  --lavender:#eef0fb;
  --star:#e8b92d;
  --white:#fff;
}
*{box-sizing:border-box;margin:0;padding:0}
html,body{width:1200px;height:4276px;overflow:hidden}
body{position:relative;font-family:"Roboto",Arial,sans-serif;color:var(--ink);background:var(--white)}
.photo{position:absolute;display:block}

/* header */
.site-header{position:absolute;left:0;top:0;width:1200px;height:77px;z-index:5}
.header-bar{position:absolute;left:157px;top:0;width:883px;height:77px;background:var(--white);display:flex}
.brand{display:flex;align-items:center;gap:10px;padding-left:14px;width:236px}
.brand-mark{width:34px;height:34px;border-radius:50%;background:var(--navy)}
.brand-name{font-weight:700;font-size:22px;color:var(--blue-dark)}
.main-nav{display:flex;background:var(--blue);height:77px;width:480px}
.main-nav a{display:flex;align-items:center;padding:0 13px;color:var(--white);font-size:11px;font-weight:700;text-decoration:none;letter-spacing:.3px;white-space:nowrap}
.main-nav a.active{background:var(--nav-active)}
.social{flex:1;background:var(--navy);display:flex;align-items:center;justify-content:center;gap:12px}
.social span{width:30px;height:30px;border:2px solid var(--white);border-radius:50%;display:flex;align-items:center;justify-content:center}
.dropdown{position:absolute;left:445px;top:77px;width:135px;background:var(--white);box-shadow:0 2px 6px rgba(0,0,0,.15);z-index:6}
.dropdown a{display:block;padding:0 12px;height:21px;line-height:21px;font-size:9px;color:#333;text-decoration:none;border-bottom:1px solid #eee;white-space:nowrap}

/* hero */
.hero{position:absolute;left:0;top:0;width:1200px;height:584px;background:linear-gradient(180deg,#c9c7b8 0%,#8f9a85 35%,#4c5b4a 60%,#2f2b3e 100%)}
.hero-title{position:absolute;top:176px;left:0;width:1200px;text-align:center;font-size:40px;line-height:48px;font-weight:700;color:var(--white);letter-spacing:.5px}
.hero-title .accent{color:var(--hero-accent)}
.hero-title .town{color:var(--navy);text-decoration:underline}
.search{position:absolute;left:171px;top:270px;width:855px;height:60px;background:var(--white);display:flex;align-items:center;font-size:12px}
.search .label{padding:0 14px;font-weight:700}
.search .field{flex:1;padding:0 10px;color:#999;border-left:1px solid #e6e6e6;height:36px;display:flex;align-items:center;justify-content:center}
.search .field:first-of-type{border-left:0}
.search button{margin-right:10px;width:96px;height:40px;border:0;background:var(--blue);color:var(--white);font:700 12px "Roboto",sans-serif}

/* welcome */
.welcome{position:absolute;left:0;top:584px;width:1200px;height:442px}
.welcome h1{position:absolute;left:171px;top:110px;font-size:29px;font-weight:700}
.welcome p{position:absolute;left:171px;top:172px;width:430px;font-size:11.5px;line-height:1.6;color:var(--body)}
.btn{display:inline-block;color:var(--white);font-size:11px;font-weight:500;text-align:center;text-decoration:none}
.read-more{position:absolute;left:524px;top:302px;width:75px;height:26px;line-height:26px;background:var(--blue);border-radius:2px}
.video-badge{position:absolute;left:889px;top:755px;width:102px;height:100px;background:var(--green);display:flex;align-items:center;justify-content:center}

/* categories */
.categories{position:absolute;left:0;top:1026px;width:1200px;height:570px;background:var(--lavender)}
.cat-label{position:absolute;top:504px;width:271px;text-align:center;font-size:16px;font-weight:700}

/* listings */
.section-title{position:absolute;left:171px;font-size:24px;font-weight:700}
.card-name{position:absolute;font-size:11px;font-weight:700;white-space:nowrap}
.stars{position:absolute;font-size:12px;color:var(--star);letter-spacing:1px}
.card-desc{position:absolute;width:190px;font-size:10px;font-style:italic;color:var(--muted);line-height:1.4}
.next-arrow{position:absolute;left:1048px}

/* banner */
.banner{position:absolute;left:0;top:2209px;width:1200px;height:527px;background:linear-gradient(120deg,#b4652a 0%,#9a4a22 45%,#c17a34 100%)}
.banner h2{position:absolute;left:171px;top:213px;width:360px;font-size:29px;line-height:1.3;color:var(--white);font-weight:700}
.banner .sub{position:absolute;left:171px;top:311px;font-size:17px;color:#f2d6bd}
.book-now{position:absolute;left:171px;top:359px;width:134px;height:36px;line-height:36px;background:var(--green)}

/* things to do */
.feature{position:absolute;left:171px;top:3449px;width:490px;height:265px;background:linear-gradient(135deg,#e8402c,#f2662c)}
.feature h3{position:absolute;left:88px;top:94px;font-size:15px;color:var(--white)}
.feature p{position:absolute;left:186px;top:134px;width:200px;font-size:10px;color:#ffe0d4;line-height:1.4}

/* newsletter */
.newsletter-title{position:absolute;left:0;top:4104px;width:1200px;text-align:center;font-size:11px;font-weight:700;letter-spacing:.5px}
.newsletter input{position:absolute;left:362px;top:4138px;width:316px;height:32px;border:1px solid #e4e4e4;padding:0 12px;font:11px "Roboto",sans-serif;color:#999}
.newsletter button{position:absolute;left:693px;top:4138px;width:142px;height:32px;border:0;background:var(--blue);color:var(--white);font:700 11px "Roboto",sans-serif}

.site-footer{position:absolute;left:0;top:4232px;width:1200px;height:44px;background:var(--navy);color:#cfd3da;font-size:10px;display:flex;align-items:center;justify-content:center;letter-spacing:.5px}
</style>
</head>
<body>

<section class="hero" role="img" aria-label="Aerial photograph of the harbour town, beaches and island at sunset">
  <h2 class="hero-title">COME, <span class="accent">DISCOVER</span> <span class="town">DORRIN</span></h2>
  <form class="search">
    <span class="label">Find</span>
    <span class="field">Hotels</span>
    <span class="field">Restaurants</span>
    <span class="field">Things To Do</span>
    <button type="button">SEARCH</button>
  </form>
</section>

<header class="site-header">
  <div class="header-bar">
    <div class="brand"><span class="brand-mark"></span><span class="brand-name">Harbourline</span></div>
    <nav class="main-nav">
      <a class="active" href="#">HOME</a>
      <a href="#">WHERE TO STAY</a>
      <a href="#">WHERE TO EAT</a>
      <a href="#">WHAT TO DO</a>
      <a href="#">CONTACT</a>
    </nav>
    <div class="social">
      <span></span><span></span>
      <span><svg width="14" height="10" viewBox="0 0 14 10"><rect x="0.5" y="0.5" width="13" height="9" fill="#fff"/><path d="M1 1l6 5 6-5" fill="none" stroke="#1c2431" stroke-width="1.2"/></svg></span>
    </div>
  </div>
  <div class="dropdown">
    <a href="#">BED &amp; BREAKFAST</a>
    <a href="#">CARAVAN &amp; CAMPING</a>
    <a href="#">GUEST HOUSES</a>
    <a href="#">HOTELS</a>
  </div>
</header>

<section class="welcome">
  <h1>Welcome to DORRIN</h1>
  <p>The jewel in the crown of Carrowshire. A popular harbour town visited by over 250,000 visitors a year. Surrounded by its medieval stone wall, Dorrin is steeped with history and beautiful landscapes. Famed for it's beautiful beaches and views that will lure you to come back each year, we hope you enjoy your time visiting and breathing in the sea air of Dorrin.</p>
  <a class="btn read-more" href="#">Read More</a>
  <div class="photo" style="left:684px;top:0;width:516px;height:442px;background:linear-gradient(160deg,#c9b04a,#c96b4c 55%,#8d8f6a)" role="img" aria-label="Crowd running into the sea at a festive beach swim"></div>
</section>
<div class="video-badge"><svg width="40" height="28" viewBox="0 0 40 28"><rect x="0" y="3" width="26" height="22" rx="2" fill="#fff"/><path d="M28 14l12-9v18z" fill="#fff"/></svg></div>

<section class="categories">
  <div class="photo" style="left:171px;top:60px;width:271px;height:419px;background:linear-gradient(180deg,#e5c8f0,#b04ca8 60%,#5a3a52)" role="img" aria-label="Colourful terraced houses on a narrow street"></div>
  <div class="photo" style="left:465px;top:60px;width:270px;height:419px;background:linear-gradient(180deg,#8fae4f,#8a6a4e 55%,#4a3326)" role="img" aria-label="Plated dish garnished with herbs"></div>
  <div class="photo" style="left:755px;top:60px;width:271px;height:419px;background:linear-gradient(180deg,#d9c9b4,#efe6da 60%,#9f8c7a)" role="img" aria-label="Breakfast table with tea cup and flowers"></div>
  <div class="cat-label" style="left:171px">Things To Do</div>
  <div class="cat-label" style="left:465px">Places To Eat</div>
  <div class="cat-label" style="left:755px">Where To Stay</div>
</section>

<h2 class="section-title" style="top:1633px">Hot Stays</h2>
<div class="photo" style="left:171px;top:1684px;width:271px;height:419px;background:linear-gradient(180deg,#b9c4cf,#8a8d94 60%,#556b46)" role="img" aria-label="Grey stone hotel building"></div>
<div class="photo" style="left:465px;top:1684px;width:270px;height:419px;background:linear-gradient(180deg,#c6b78e,#7d7467 55%,#5b5a4a)" role="img" aria-label="Group of campers at a holiday park"></div>
<div class="photo" style="left:755px;top:1684px;width:271px;height:419px;background:linear-gradient(180deg,#7fb2d9,#d8c39a 45%,#7a8a6a)" role="img" aria-label="Pastel townhouse guest house"></div>
<svg class="next-arrow" style="top:1880px" width="32" height="24" viewBox="0 0 32 24"><path d="M2 12h27M19 2l10 10-10 10" fill="none" stroke="#222" stroke-width="2"/></svg>
<div class="card-name" style="left:171px;top:2120px">Seawall Hotel</div><div class="stars" style="left:385px;top:2118px">★★★★</div>
<div class="card-desc" style="left:171px;top:2137px">Lorem ipsum dolor sit amet, consectetur adipiscing elit</div>
<div class="card-name" style="left:465px;top:2120px">Cliffside Holiday Park</div><div class="stars" style="left:677px;top:2118px">★★★★</div>
<div class="card-desc" style="left:465px;top:2137px">Lorem ipsum dolor sit amet, consectetur adipiscing elit</div>
<div class="card-name" style="left:755px;top:2120px">Marlowe House</div><div class="stars" style="left:968px;top:2118px">★★★★</div>
<div class="card-desc" style="left:755px;top:2137px">Lorem ipsum dolor sit amet, consectetur adipiscing elit</div>

<section class="banner" role="img" aria-label="Shopping street with sweet shop fronts, tinted orange">
  <h2>Lorem ipsum dolor sit amet, consectetur</h2>
  <div class="sub">Sed do eiusmod tempor incididunt</div>
  <a class="btn book-now" href="#">BOOK NOW</a>
</section>

<h2 class="section-title" style="top:2790px">Top 15 Restaurants</h2>
<div class="photo" style="left:171px;top:2841px;width:271px;height:422px;background:linear-gradient(180deg,#d8b48a,#9a5f3c 55%,#5b3a28)" role="img" aria-label="Restaurant interior with wooden tables"></div>
<div class="photo" style="left:465px;top:2841px;width:270px;height:422px;background:linear-gradient(180deg,#e9d6b6,#c98f5e 50%,#3d3230)" role="img" aria-label="Diners sharing a meal"></div>
<div class="photo" style="left:755px;top:2841px;width:271px;height:422px;background:linear-gradient(180deg,#9fbf8a,#3a78b4 50%,#c9c0a8)" role="img" aria-label="Restaurant entrance with blue door and flowers"></div>
<svg class="next-arrow" style="top:3040px" width="32" height="24" viewBox="0 0 32 24"><path d="M2 12h27M19 2l10 10-10 10" fill="none" stroke="#222" stroke-width="2"/></svg>
<div class="card-name" style="left:171px;top:3280px">Tidewater Restaurant</div><div class="stars" style="left:385px;top:3278px">★★★★</div>
<div class="card-desc" style="left:171px;top:3297px">Lorem ipsum dolor sit amet, consectetur adipiscing elit</div>
<div class="card-name" style="left:465px;top:3280px">Lantern Restaurant</div><div class="stars" style="left:677px;top:3278px">★★★★</div>
<div class="card-desc" style="left:465px;top:3297px">Lorem ipsum dolor sit amet, consectetur adipiscing elit</div>
<div class="card-name" style="left:755px;top:3280px">Rampart Restaurant</div><div class="stars" style="left:968px;top:3278px">★★★★</div>
<div class="card-desc" style="left:755px;top:3297px">Lorem ipsum dolor sit amet, consectetur adipiscing elit</div>

<h2 class="section-title" style="top:3392px">Things To Do</h2>
<div class="feature" role="img" aria-label="Outdoor activity scene tinted red">
  <h3>Lorem ipsum dolor sit amet</h3>
  <p>Consectetur adipiscing elit, sed do eiusmod tempor incididunt ut labore magna aliqua.</p>
</div>
<div class="photo" style="left:684px;top:3449px;width:342px;height:564px;background:linear-gradient(180deg,#7fb0c4,#c9bfa6 30%,#3a5fa0 60%,#7a3a3a)" role="img" aria-label="Visitor posing above a sandy beach"></div>
<div class="photo" style="left:171px;top:3739px;width:199px;height:274px;background:linear-gradient(160deg,#7ec9e8,#2a3a4a 60%,#1a82b8)" role="img" aria-label="Cyclist adjusting a bike"></div>
<div class="photo" style="left:393px;top:3739px;width:268px;height:274px;background:linear-gradient(180deg,#bcd4e8,#d89a6a 40%,#5a8fb0)" role="img" aria-label="Harbour with colourful boats and houses"></div>

<section class="newsletter">
  <div class="newsletter-title">RECEIVE LATEST UPDATES FROM US</div>
  <input type="text" value="Email id" aria-label="Email address">
  <button type="button">SUBMIT</button>
</section>

<footer class="site-footer">COPYRIGHT INFO</footer>

</body>
</html>
```